Business card design for strategy and management consulting company. Would like to have a clean and professional business card, based on the attached logo. The company is a strategy and management consulting company focusing on sustainable business modlels based on economic, social and environmental market opportunities. Preferably the logo should be included on both sides of the design.

Industry/Entity Type

Business

Contact Information for Business Card

Halvor Brekkeli, CEO/Management consultant
halvor.brekkeli@morvikpartners.example
Mob: +47 936 28 417
Office: Lyngvedens gate 14, pb 312 sentrum, N-0158 Oslo Norway

Requirements
Must have
• Include attached logo
Nice to have
• Would like to have the logo on both sides
Should not have
• Many colours.

```html
<!DOCTYPE html>
<html lang="en">
<head>
<meta charset="utf-8">
<title>Morvik business card</title>
<link rel="stylesheet" href="https://fonts.googleapis.com/css2?family=Lato:wght@400;700&display=swap">
<style>
  :root {
    --ink: #1b1b1b;
    --paper: #ffffff;
    --accent: #f7d417;
    --accent-text: #d9b800;
    --text-dark: #222222;
    --backdrop: #8e8e8c;
  }
  * { box-sizing: border-box; margin: 0; padding: 0; }
  html, body { width: 1200px; height: 799px; overflow: hidden; }
  body {
    background: var(--backdrop);
    font-family: "Lato", Arial, sans-serif;
    display: flex;
    align-items: center;
    justify-content: center;
    gap: 40px;
  }
  .card {
    position: relative;
    width: 540px;
    height: 309px;
    overflow: hidden;
    background: var(--ink);
  }
  .card-shapes { position: absolute; inset: 0; }

  .brand {
    position: absolute;
    display: flex;
    align-items: center;
    gap: 8px;
    color: var(--paper);
    font-weight: 700;
    line-height: 1;
    white-space: nowrap;
  }
  .brand-mark { width: 8px; height: 8px; background: var(--accent); }

  /* Back side */
  .card-back .brand { left: 272px; top: 112px; font-size: 52px; }
  .card-back .brand-site {
    position: absolute; left: 274px; top: 174px;
    color: var(--accent); font-size: 15px;
  }

  /* Front side */
  .card-front .brand { left: 372px; top: 14px; font-size: 40px; }
  .social-handle {
    position: absolute; right: 14px; top: 66px;
    font-size: 12px; font-weight: 700; color: var(--ink);
  }
  .contact {
    position: absolute; left: 26px; top: 104px;
    color: var(--text-dark);
  }
  .contact-name { font-size: 21px; font-weight: 400; line-height: 1.2; }
  .contact-role { font-size: 12px; color: var(--accent-text); margin-top: 1px; }
  .contact-list { list-style: none; margin-top: 11px; font-size: 12.5px; line-height: 1.35; }
  .contact-list li { display: flex; align-items: flex-start; gap: 9px; margin-bottom: 3px; }
  .contact-list svg { flex: none; margin-top: 2px; }
  .front-site {
    position: absolute; left: 26px; top: 252px;
    color: var(--accent); font-size: 15px;
  }
</style>
</head>
<body>

  <section class="card card-back" aria-label="Card back">
    <div class="brand"><span class="brand-name">Morvik</span><span class="brand-mark"></span></div>
    <div class="brand-site">morvikpartners.example</div>
  </section>

  <section class="card card-front" aria-label="Card front">
    <svg class="card-shapes" width="540" height="309" viewBox="0 0 540 309" aria-hidden="true">
      <!-- white body under the sweep -->
      <path d="M0 100 Q180 72 360 66 L540 66 L540 309 L0 309 Z" fill="var(--paper)"/>
      <!-- yellow sweep joining the band -->
      <path d="M0 100 Q180 72 360 66" fill="none" stroke="var(--accent)" stroke-width="6"/>
      <rect x="358" y="62" width="182" height="22" fill="var(--accent)"/>
      <!-- website strip and white foot -->
      <rect x="0" y="240" width="470" height="46" fill="var(--ink)"/>
    </svg>

    <div class="brand"><span class="brand-name">Morvik</span><span class="brand-mark"></span></div>
    <div class="social-handle">/morvik</div>

    <div class="contact">
      <h1 class="contact-name">Halvor Brekkeli</h1>
      <p class="contact-role">CEO/Management consultant</p>
      <ul class="contact-list">
        <li>
          <svg width="12" height="12" viewBox="0 0 12 12" aria-hidden="true"><path d="M2 1 L4.5 1 L5.5 3.5 L4 4.5 Q5 7 7.5 8 L8.5 6.5 L11 7.5 L11 10 Q6 11 1 5 Q1 2.5 2 1 Z" fill="var(--accent)"/></svg>
          <span>+47 936 28 417</span>
        </li>
        <li>
          <svg width="12" height="12" viewBox="0 0 12 12" aria-hidden="true"><rect x="0.5" y="2.5" width="11" height="7.5" fill="var(--accent)"/><path d="M0.5 2.5 L6 7 L11.5 2.5" fill="none" stroke="var(--paper)" stroke-width="1"/></svg>
          <span>halvor.brekkeli@morvikpartners.example</span>
        </li>
        <li>
          <svg width="12" height="12" viewBox="0 0 12 12" aria-hidden="true"><path d="M6 11.5 Q1.5 6.5 1.5 4.5 A4.5 4.5 0 0 1 10.5 4.5 Q10.5 6.5 6 11.5 Z" fill="var(--accent)"/><circle cx="6" cy="4.5" r="1.6" fill="var(--paper)"/></svg>
          <span>Lyngvedens gate 14,<br>pb 312 sentrum, Oslo Norway</span>
        </li>
      </ul>
    </div>

    <div class="front-site">morvikpartners.example</div>
  </section>

</body>
</html>
```